Social Media covers for a vacation rental startup

Tivvit.com is a property management company that specializes in the short-term rental of beach houses in the coast of the Arabian Gulf (aka the Persian Gulf) in Kuwait.

Tivvit.com allows users to browse through a list of beach houses and make the booking easily. The main characteristic of tivvit is simplicity. The identity of the company is based around minimalist design with no frills.

We need a to design a facebook page. I would like to use this page for google plus and plain circle.

Check out our website on tivvit.com

Target Market(s)

People looking for short term rental in Kuwait.

Typically young mothers or young men looking to spend time with their friends.

Industry/Entity Type

It Company

Colors
3176b5
85acd3
f68e4e

Requirements
Must have
• The pictures should reflect the Kuwaiti beach environment.
Nice to have
• There should be no mountains and no palm trees.
• The environment in Kuwait does not have these elements.

```html
<!DOCTYPE html>
<html lang="en">
<head>
<meta charset="utf-8">
<title>Tivvit.com – Social Media Covers</title>
<link rel="stylesheet" href="https://fonts.googleapis.com/css2?family=Source+Sans+3:wght@300;400;600;700&display=swap">
<style>
  :root{
    --page-bg:#cce9f8;
    --ink:#111;
    --brand-blue:#3176b5;
    --brand-light:#85acd3;
    --brand-orange:#f68e4e;
    --white:#fff;
    --frame:#ffffff;
    --bar-text:#333;
    --muted:#999;
  }
  *{box-sizing:border-box;margin:0;padding:0}
  html,body{width:1200px;height:913px;overflow:hidden;background:var(--page-bg);font-family:"Source Sans 3",sans-serif;color:var(--ink)}
  .canvas{position:relative;width:1200px;height:913px}

  .brand-mark{position:absolute;left:0;top:96px;width:1200px;text-align:center;font-weight:700;font-size:26px;line-height:30px;color:var(--brand-orange)}

  .section-title{position:absolute;left:0;width:1200px;text-align:center;font-weight:400;font-size:36px;letter-spacing:0.3px}
  .section-title.templates{top:190px}
  .section-title.mockups{top:515px}

  .caption{position:absolute;width:300px;text-align:center;font-size:20px}

  .frame{position:absolute;background:var(--frame);border:3px solid var(--frame);box-shadow:0 1px 4px rgba(0,0,0,0.25)}
  .cover{position:relative;width:100%;height:187px;overflow:hidden}
  .mockup .cover{height:188px}
  .photo{position:absolute;inset:0}
  .photo.lagoon{background:linear-gradient(180deg,#2f5fb2 0%,#5b8fd0 45%,#8fc4e8 62%,#2fc3d8 72%,#1aa7d0 82%,#f1efe8 100%)}
  .photo.shore{background:linear-gradient(180deg,#2a7fd8 0%,#5aa4ea 50%,#7bbbe8 58%,#1e87c4 60%,#e4e2dc 63%,#d8d5cc 100%)}
  .streak{position:absolute;top:0;left:260px;width:150px;height:100%;background:linear-gradient(90deg,rgba(255,255,255,0) 0%,rgba(255,255,255,0.28) 50%,rgba(255,255,255,0) 100%);transform:skewX(-22deg)}

  .headline{position:absolute;font-weight:300;font-size:17px;line-height:22px}
  .headline .main{font-weight:400}
  .headline .thin{font-weight:300}
  .headline.right{right:8px;top:36px;text-align:right;color:var(--white)}
  .headline.right .rule{height:1px;background:rgba(255,255,255,0.85);margin-top:2px}
  .headline.left{left:26px;top:18px;color:#111}
  .site{font-size:10px;font-weight:400;line-height:14px;margin-top:3px}
  .headline.left .site{font-size:12px;font-weight:600;margin-top:1px}
  .social{display:flex;gap:4px;margin-top:3px}
  .headline.right .social{justify-content:flex-end}
  .social span{width:11px;height:11px;border-radius:50%;background:var(--white)}
  .headline.left .social span{width:13px;height:13px;background:#111}

  .page-bar{position:relative;height:48px;background:var(--white)}
  .avatar{position:absolute;left:14px;top:-74px;width:100px;height:104px;background:var(--page-bg);border:3px solid var(--white);box-shadow:0 1px 2px rgba(0,0,0,0.2);display:flex;align-items:center;justify-content:center}
  .avatar .name{font-weight:700;font-size:15px;color:var(--brand-orange)}
  .page-name{position:absolute;left:123px;top:10px;font-weight:700;font-size:13px;color:var(--bar-text)}
  .page-stats{position:absolute;left:123px;top:27px;font-size:6px;color:var(--muted)}
  .actions{position:absolute;right:14px;top:10px;display:flex;gap:5px}
  .btn{font-size:7px;font-weight:700;color:#333;background:#f5f6f7;border:1px solid #c5c7cc;border-radius:2px;padding:2px 5px;height:15px;display:flex;align-items:center}
</style>
</head>
<body>
<div class="canvas">

  <div class="brand-mark">Tivvit.com</div>

  <h1 class="section-title templates">Templates</h1>

  <div class="frame template" style="left:58px;top:252px;width:510px;height:187px">
    <div class="cover">
      <div class="photo lagoon" role="img" aria-label="Beach photo: white sand shore with turquoise water and a green tree line under a blue sky"></div>
      <div class="headline right">
        <div class="thin">A UNIQUE SELECTION OF</div>
        <div class="main">VERIFIED BEACH RENTALS <span class="thin">IN</span> KUWAIT</div>
        <div class="rule"></div>
        <div class="site">tivvit.com</div>
        <div class="social"><span></span><span></span></div>
      </div>
    </div>
  </div>
  <div class="frame template" style="left:644px;top:252px;width:509px;height:187px">
    <div class="cover">
      <div class="photo shore" role="img" aria-label="Beach photo: pale sand with a thatched umbrella and two sun loungers before calm blue sea"></div>
      <div class="streak"></div>
      <div class="headline left">
        <div class="thin">A UNIQUE SELECTION OF</div>
        <div class="main">VERIFIED BEACH RENTALS <span class="thin">IN</span> KUWAIT</div>
        <div class="site">tivvit.com</div>
        <div class="social"><span></span><span></span></div>
      </div>
    </div>
  </div>

  <div class="caption" style="left:126px;top:454px">Sample 1</div>
  <div class="caption" style="left:749px;top:454px">Sample 2</div>

  <h1 class="section-title mockups">Mock-ups</h1>

  <div class="frame mockup" style="left:56px;top:574px;width:513px;height:237px">
    <div class="cover">
      <div class="photo lagoon" role="img" aria-label="Beach photo: white sand shore with turquoise water and a green tree line under a blue sky"></div>
      <div class="headline right">
        <div class="thin">A UNIQUE SELECTION OF</div>
        <div class="main">VERIFIED BEACH RENTALS <span class="thin">IN</span> KUWAIT</div>
        <div class="rule"></div>
        <div class="site">tivvit.com</div>
        <div class="social"><span></span><span></span></div>
      </div>
    </div>
    <div class="page-bar">
      <div class="avatar"><div class="name">Tivvit.com</div></div>
      <div class="page-name">Shoreline Social</div>
      <div class="page-stats">1,238 likes · 18 talking about this</div>
      <div class="actions"><div class="btn">Update Page Info</div><div class="btn">✓ Liked</div><div class="btn">⚙ ▾</div></div>
    </div>
  </div>

  <div class="frame mockup" style="left:645px;top:574px;width:512px;height:237px">
    <div class="cover">
      <div class="photo shore" role="img" aria-label="Beach photo: pale sand with a thatched umbrella and two sun loungers before calm blue sea"></div>
      <div class="streak"></div>
      <div class="headline left">
        <div class="thin">A UNIQUE SELECTION OF</div>
        <div class="main">VERIFIED BEACH RENTALS <span class="thin">IN</span> KUWAIT</div>
        <div class="site">tivvit.com</div>
        <div class="social"><span></span><span></span></div>
      </div>
    </div>
    <div class="page-bar">
      <div class="avatar"><div class="name">Tivvit.com</div></div>
      <div class="page-name">Shoreline Social</div>
      <div class="page-stats">1,238 likes · 18 talking about this</div>
      <div class="actions"><div class="btn">Update Page Info</div><div class="btn">✓ Liked</div><div class="btn">⚙ ▾</div></div>
    </div>
  </div>

  <div class="caption" style="left:124px;top:826px">Sample 1</div>
  <div class="caption" style="left:747px;top:826px">Sample 2</div>

</div>
</body>
</html>
```